Pipelining Product Supply Company Needs New Stationery

We need new stationery (letter head, with compliments slips & business card) for our industry leading pipe lining supply company. basically we sell product to other plumbers to carry out pipe relining.

Im looking for something, fresh, professional, sleek and modern at the same time.

Ive attached a copy of the logo and also some guidelines to follow for colours and fonts etc.

Target Market(s)

Plumbers

Industry/Entity Type

Plumbing

Font styles to use
Sans Serif

Requirements
Must have
• The logo, space for ABN, Address, Phone Number, website and email.
Nice to have
• Stand out from the crowd. To look sleep and professional.
Should not have
• Any other colours apart from what is on the guidelines.

```html
<!DOCTYPE html>
<html lang="en">
<head>
<meta charset="utf-8">
<title>Tarrow Pipe Supply – Business Card</title>
<link href="https://fonts.googleapis.com/css2?family=Lato:wght@400;700&family=Roboto:wght@400&display=swap" rel="stylesheet">
<style>
  :root {
    --backdrop: #262626;
    --card-grey: #9d9ea2;
    --card-white: #f4f4f4;
    --green-deep: #0f5a12;
    --green-mid: #3f9a2a;
    --green-light: #8cc63f;
    --text-white: #ffffff;
    --logo-green: #4c9e2f;
  }
  * { margin: 0; padding: 0; box-sizing: border-box; }
  html, body { width: 1200px; height: 960px; overflow: hidden; }
  body {
    background: var(--backdrop);
    position: relative;
    font-family: "Lato", sans-serif;
  }
  .card {
    position: absolute;
    width: 600px;
    height: 343px;
    border-radius: 20px;
    overflow: hidden;
  }
  .card-front { left: 302px; top: 128px; background: var(--card-white); }
  .card-back {
    left: 300px; top: 488px;
    background: radial-gradient(ellipse 62% 70% at 50% 52%, var(--green-light) 0%, var(--green-mid) 45%, var(--green-deep) 100%);
  }
  .front-shapes { position: absolute; inset: 0; }
  .contact {
    position: absolute;
    left: 46px;
    top: 90px;
    color: var(--text-white);
  }
  .contact-name { font-size: 22px; font-weight: 400; letter-spacing: 0.3px; line-height: 1; }
  .contact-role { font-size: 14px; margin-top: 5px; }
  .contact-address { font-size: 13.5px; line-height: 17px; margin-top: 12px; }
  .contact-lines { list-style: none; margin-top: 10px; font-size: 13.5px; line-height: 18.5px; }
  .contact-lines li { display: flex; align-items: center; gap: 8px; }
  .contact-lines svg { width: 12px; height: 12px; fill: var(--text-white); flex: none; }
  .brand-front {
    position: absolute;
    right: 38px;
    top: 44px;
    width: 230px;
    text-align: center;
    color: var(--logo-green);
    font-weight: 700;
    line-height: 1;
  }
  .brand-front .brand-main { display: block; font-size: 50px; letter-spacing: 2px; }
  .brand-front .brand-sub { display: block; font-size: 19px; letter-spacing: 1px; margin-top: 8px; }
  .brand-back {
    position: absolute;
    left: 0; right: 0;
    top: 104px;
    text-align: center;
    color: var(--green-light);
    font-weight: 700;
    font-size: 92px;
    letter-spacing: 4px;
    line-height: 1;
  }
  .back-web {
    position: absolute;
    left: 0; right: 0;
    top: 217px;
    text-align: center;
    font-family: "Roboto", sans-serif;
    font-size: 14px;
    letter-spacing: 1.6px;
    color: var(--text-white);
  }
</style>
</head>
<body>
  <section class="card card-front">
    <svg class="front-shapes" viewBox="0 0 600 343" width="600" height="343" aria-hidden="true">
      <path d="M0 0 H228 C250 120 340 260 482 343 H0 Z" fill="var(--card-grey)"/>
      <path d="M240 0 H268 C268 120 360 260 488 343 H482 C330 262 246 130 240 0 Z" fill="var(--logo-green)"/>
      <path d="M228 0 H240 C246 130 330 262 482 343 H478 C336 262 248 126 228 0 Z" fill="#ffffff"/>
    </svg>
    <div class="contact">
      <p class="contact-name">MARA ELLISON</p>
      <p class="contact-role">CEO/FOUNDER</p>
      <p class="contact-address">214 Wattle Grove Road<br>Ballarat, Victoria 3350<br><span style="display:inline-block;margin-top:6px">ABN: 4820193756</span></p>
      <ul class="contact-lines">
        <li><svg viewBox="0 0 24 24"><path d="M6.6 10.8a15 15 0 0 0 6.6 6.6l2.2-2.2c.3-.3.7-.4 1-.2 1.1.4 2.3.6 3.6.6.6 0 1 .4 1 1V20c0 .6-.4 1-1 1A17 17 0 0 1 3 4c0-.6.4-1 1-1h3.5c.6 0 1 .4 1 1 0 1.3.2 2.5.6 3.6.1.3 0 .7-.2 1z"/></svg>613 582 0947</li>
        <li><svg viewBox="0 0 24 24"><path d="M2 5h20v14H2z M2 5l10 8 10-8" stroke="#9d9ea2" stroke-width="1.6"/></svg>hello@tarrowsupply.com</li>
        <li><svg viewBox="0 0 24 24"><circle cx="12" cy="12" r="10"/><path d="M2 12h20M12 2c3 3 3 17 0 20M12 2c-3 3-3 17 0 20" stroke="#9d9ea2" stroke-width="1.4" fill="none"/></svg>www.tarrowsupply.com</li>
      </ul>
    </div>
    <p class="brand-front"><span class="brand-main">TARROW</span><span class="brand-sub">PIPE SUPPLY</span></p>
  </section>

  <section class="card card-back">
    <p class="brand-back">TARROW</p>
    <p class="back-web">www.tarrowpipesupply.com</p>
  </section>
</body>
</html>
```